I am a surgeon that operates on gynaecological cancer. Wish a design and logo for letter head.

Design should include my name: Dr. Torin Halwell, qualifications: FKMLTPVB, DMR. and state that I am a Gynaecological Oncologist and Advanced Laparoscopic Surgeon.
As for a logo. As all cancer is related to DNA, I think that that double helix could be used to symbolise a female shape, exaggerating the abdomen to suggest a mass.

Reason: Extended to view changes I have asked for.

```html
<!DOCTYPE html>
<html lang="en">
<head>
<meta charset="utf-8">
<title>Dr. Torin Halwell – Letterhead</title>
<link rel="stylesheet" href="https://fonts.googleapis.com/css2?family=Crimson+Text:wght@400&display=swap">
<style>
  :root {
    --canvas-bg: #ffffff;
    --page-border: #4a4a4a;
    --rule-grey: #cfcfcf;
    --name-teal: #137f80;
    --quals-grey: #8a8a8a;
    --tagline-cyan: #1ba8d2;
    --mark-green: #8cc63f;
  }
  html, body {
    margin: 0;
    padding: 0;
    width: 1200px;
    height: 1000px;
    overflow: hidden;
    background: var(--canvas-bg);
    font-family: "Crimson Text", "Palatino Linotype", Georgia, serif;
  }
  .letterhead {
    position: absolute;
    left: 258px;
    top: 60px;
    width: 679px;
    height: 882px;
    border: 1px solid var(--page-border);
    background: #fff;
  }
  .doctor-name {
    position: absolute;
    right: 111px;
    top: 44px;
    margin: 0;
    font-size: 35px;
    font-weight: 400;
    color: var(--name-teal);
    line-height: 1;
    white-space: nowrap;
  }
  .qualifications {
    position: absolute;
    right: 111px;
    top: 91px;
    margin: 0;
    font-size: 14px;
    color: var(--quals-grey);
    line-height: 1;
  }
  .header-rule {
    position: absolute;
    left: 28px;
    width: 563px;
    height: 0;
    border-top: 1px solid var(--rule-grey);
  }
  .header-rule.upper { top: 114px; }
  .header-rule.lower { top: 137px; }
  .specialty {
    position: absolute;
    right: 105px;
    top: 118px;
    margin: 0;
    font-size: 14.5px;
    color: var(--tagline-cyan);
    line-height: 1;
    white-space: nowrap;
  }
  .side-rule {
    position: absolute;
    left: 646px;
    top: 290px;
    height: 572px;
    border-left: 1px solid var(--rule-grey);
  }
  .brand-mark {
    position: absolute;
    left: 582px;
    top: 200px;
    width: 92px;
    text-align: center;
  }
  .brand-mark .brand-dot {
    display: block;
    margin: 0 auto 6px;
    width: 14px;
    height: 14px;
    border-radius: 50%;
    background: var(--mark-green);
  }
  .brand-mark .brand-name {
    font-size: 13px;
    color: var(--mark-green);
    white-space: nowrap;
  }
</style>
</head>
<body>
  <div class="letterhead">
    <h1 class="doctor-name">Dr. Torin Halwell</h1>
    <p class="qualifications">FKMLTPVB, DMR</p>
    <div class="header-rule upper"></div>
    <p class="specialty">Gynecological Oncologist and Advanced Laparoscopic Surgeon.</p>
    <div class="header-rule lower"></div>
    <div class="brand-mark">
      <span class="brand-dot"></span>
      <span class="brand-name">Torin Halwell</span>
    </div>
    <div class="side-rule"></div>
  </div>
</body>
</html>
```